Small Business Broker Business Card Design

A business card design for a small business brokerage, which is a financial service, not unlike real estate brokerage, but for small businesses such as laundromats, pizza shops, restaurants, cleaners etc. The designs should all be simple, more conservative in nature, using the colors and font of the logo. Again, think real estate Brokerage as a business context
Contact Information for Business Card
Name: Dale R. Whitmore. Title: Small Business Advisor. Email: d.whitmore@lanternbridgeadvisory.com. Mobile: (917) 555-0148. Office: (718) 555-0193. www.lanternbridgeadvisory.com

```html
<!DOCTYPE html>
<html lang="en">
<head>
<meta charset="utf-8">
<title>Lanternbridge Advisory — Business Card</title>
<link href="https://fonts.googleapis.com/css2?family=Montserrat:wght@400;500;600;700&display=swap" rel="stylesheet">
<style>
  :root {
    --navy: #1c3868;
    --navy-deep: #17305a;
    --green: #8cc63f;
    --white: #ffffff;
    --backdrop: #e4e3e4;
  }
  * { margin: 0; padding: 0; box-sizing: border-box; }
  html, body {
    width: 1200px; height: 1108px; overflow: hidden;
    background: var(--backdrop);
    font-family: "Montserrat", sans-serif;
  }
  .card {
    position: absolute;
    width: 740px; height: 443px;
    background: var(--navy);
    overflow: hidden;
  }
  .card--front { left: 241px; top: 68px; }
  .card--back { left: 248px; top: 589px; }

  .front-art { position: absolute; inset: 0; }

  .company { position: absolute; left: 30px; top: 46px; }
  .company__name {
    color: var(--white); font-weight: 600; font-size: 19.5px;
    letter-spacing: 0.3px; line-height: 1;
  }
  .company__tagline {
    margin-top: 4px; color: var(--green); font-weight: 600;
    font-size: 10.5px; letter-spacing: 1.3px; line-height: 1;
  }

  .person { position: absolute; left: 32px; top: 214px; }
  .person__name {
    font-weight: 700; font-size: 27px; line-height: 1; color: var(--white);
  }
  .person__name .given { color: var(--green); }
  .person__title {
    margin-top: 5px; color: var(--white); font-size: 16px; font-weight: 400;
  }

  .contacts { position: absolute; left: 34px; top: 311px; list-style: none; }
  .contacts li {
    display: flex; align-items: center; height: 24px;
    color: var(--white); font-size: 16px; font-weight: 400;
  }
  .contacts li:nth-child(2) { margin-top: 6px; }
  .contacts svg { width: 15px; height: 15px; margin-right: 13px; fill: var(--green); }

  .brand-name {
    position: absolute; left: 458px; top: 214px; width: 270px;
    text-align: center; color: var(--navy);
    font-weight: 700; font-size: 23px; letter-spacing: 1px; line-height: 1.15;
  }

  .back-brand {
    position: absolute; left: 0; right: 0; top: 276px; text-align: center;
    color: var(--navy-deep);
  }
  .back-brand__name { font-weight: 500; font-size: 24px; letter-spacing: 1px; line-height: 1; }
  .back-brand__tagline { margin-top: 6px; font-size: 12.5px; font-weight: 500; letter-spacing: 2px; }
</style>
</head>
<body>

<section class="card card--front">
  <svg class="front-art" viewBox="0 0 740 443" width="740" height="443" aria-hidden="true">
    <path d="M526 0 C300 110 300 340 530 443 L740 443 L740 0 Z" fill="#ffffff"/>
    <path d="M516 22 C338 140 338 330 512 420 C360 322 360 150 516 22 Z" fill="#8cc63f"/>
  </svg>

  <div class="company">
    <p class="company__name">LANTERNBRIDGE ADVISORY, INC</p>
    <p class="company__tagline">TRUSTED GUIDANCE TO BUY OR SELL YOUR BUSINESS</p>
  </div>

  <div class="person">
    <h1 class="person__name"><span class="given">Dale R.</span> Whitmore</h1>
    <p class="person__title">Small Business Advisor</p>
  </div>

  <ul class="contacts">
    <li>
      <svg viewBox="0 0 16 16"><path d="M1 6c0-2 3-3.5 7-3.5S15 4 15 6v1.5h-3.5V6H4.5v1.5H1z"/><path d="M3 9l2-2h6l2 2v4H3z"/></svg>
      (718) 555-0193
    </li>
    <li>
      <svg viewBox="0 0 16 16"><path d="M3.5 1l2.5 3-1.5 1.8c.8 2 2.5 3.8 4.5 4.7L10.8 9l3.2 2.4-1.5 2.8C7 14 2 9 1.5 3.4z"/></svg>
      (917) 555-0148
    </li>
    <li>
      <svg viewBox="0 0 16 16"><path d="M1 3.5h14v1.2L8 9 1 4.7z"/><path d="M1 6.3l7 4.3 7-4.3V12.5H1z"/></svg>
      d.whitmore@lanternbridgeadvisory.com
    </li>
    <li>
      <svg viewBox="0 0 16 16"><circle cx="8" cy="8" r="6.5"/></svg>
      www.lanternbridgeadvisory.com
    </li>
  </ul>

  <p class="brand-name">LANTERNBRIDGE</p>
</section>

<section class="card card--back">
  <div class="back-brand">
    <p class="back-brand__name">LANTERNBRIDGE ADVISORY, INC</p>
    <p class="back-brand__tagline">TRUSTED GUIDANCE TO BUY OR SELL YOUR BUSINESS</p>
  </div>
</section>

</body>
</html>
```